Turfbloom.com needs a professional yet bold design to share our differences and convert customers!

We need web design for the only company to offer same day & next day lawn care services to the North Carolina Piedmont Triad area! Customers will be able to view cost and book their lawn service in 5 minutes via our website. We need to promote the following that set us apart: 1: No Contract 2: Instant Scheduling 3: Same Day Service 4: Fully Licensed and Insured, 5: Money Back Guarantee. We are the ONLY company in the area to offer this service.
The site needs to be bold to show the reasons we are different. "in your face", yet professional enough to earn a customer's trust. Inspiration can be drawn from sites such as tidyfoxcrew.com, however the creative piece will be up to you to create a website that is perhaps unique, slightly tacky, different, etc. The key is for it to be the BEST in the area and easy to use without confusing customers. Must be able to allure customers in and have an easy checkout and booking procedure.
Updates

Target Market(s)

People that want a simple, quick, and easy way to get someone to mow their grass!

Industry/Entity Type

It Company

Logo Text

Turf Bloom logo design opportunity to be offered as well.

Number of Pages Required

1 page

Requirements
Must have
• simple, bold, yet instill trust from the public.
Nice to have
• Need chat now, book now, popups showing % off that day. Need Zip code entry to price lawns. Need it to emphasize the quick process, reliability of the company, etc.

```html
<!DOCTYPE html>
<html lang="en">
<head>
<meta charset="utf-8">
<title>Turf Bloom — Same Day &amp; Next Day Lawn Care</title>
<link href="https://fonts.googleapis.com/css2?family=Open+Sans:wght@400;600&family=Roboto:wght@400;500;700&display=swap" rel="stylesheet">
<style>
:root{
  --ink:#1e1e1e;
  --text:#555;
  --blue:#1a8bd6;
  --dark:#2b2b2b;
  --line:#dcdcdc;
  --paper:#f7f7f7;
  --footer:#f1f1f1;
  --bar:#232323;
  --white:#fff;
  --social:#555;
  --photo-paper:#d9d6cf;
  --photo-sky:#8cc9e8;
  --photo-grass:#5a9e30;
  --photo-hedge:#4f8fcf;
  --photo-seal:#3f8fc6;
}
*{box-sizing:border-box;margin:0;padding:0}
html,body{width:1200px;height:2835px;overflow:hidden}
body{font-family:"Open Sans",Arial,sans-serif;color:var(--text);background:var(--white);position:relative}

/* header */
.site-header{position:absolute;top:0;left:0;width:1200px;height:119px;background:linear-gradient(#f4f4f4,#fff 40%)}
.brand{position:absolute;left:100px;top:36px;display:flex;align-items:center;gap:14px;font-family:"Roboto",sans-serif;font-size:40px;font-weight:400;color:var(--ink)}
.brand-dot{width:40px;height:40px;border-radius:50%;background:var(--ink)}
.main-nav{position:absolute;right:98px;top:54px;display:flex;font-family:"Roboto",sans-serif;font-size:13px;color:var(--ink)}
.main-nav a{color:inherit;text-decoration:none;padding:0 22px;border-left:1px solid var(--line)}
.main-nav a:first-child{border-left:0}
.main-nav a:last-child{padding-right:0}

/* hero */
.hero{position:absolute;top:119px;left:0;width:1200px;height:469px}
.hero-bg{position:absolute;inset:0;background:linear-gradient(180deg,#cfe3ea 0%,#e9f0f0 45%,#dfe4e6 72%,#b9c3c7 100%)}
.hero-title{position:absolute;left:98px;top:95px;font-family:"Roboto",sans-serif;font-weight:700;font-size:39px;line-height:47px;color:var(--ink)}
.hero-copy{position:absolute;left:98px;top:200px;width:470px;font-size:12.5px;line-height:21px;color:#333}
.btn-dark{display:inline-block;background:var(--dark);color:var(--white);font-family:"Roboto",sans-serif;font-size:14px;border-radius:3px;text-decoration:none}
.hero-cta{position:absolute;left:100px;top:343px;padding:10px 22px}
.video{position:absolute;left:614px;top:85px;width:488px;height:300px;background:linear-gradient(120deg,#4f8d2c 0%,#6aa638 60%,#5a8f2e 100%)}
.video-play{position:absolute;left:208px;top:120px;width:56px;height:36px;background:rgba(20,20,20,.85);border-radius:3px}
.video-play svg{position:absolute;left:20px;top:10px}
.video-bar{position:absolute;left:16px;right:16px;bottom:14px;height:20px;background:rgba(20,20,20,.8);border-radius:2px}
.video-progress{position:absolute;left:10px;top:8px;width:330px;height:4px;background:#555}
.video-progress span{display:block;width:150px;height:4px;background:var(--blue)}

/* booking band */
.booking{position:absolute;top:588px;left:0;width:1200px;height:123px;background:var(--blue);color:var(--white)}
.booking-title{position:absolute;left:98px;top:24px;font-family:"Roboto",sans-serif;font-size:21px;font-weight:400}
.booking-copy{position:absolute;left:98px;top:56px;width:520px;font-size:12px;line-height:19px}
.zip-field{position:absolute;left:644px;top:38px;width:330px;height:44px;background:var(--white);border-radius:3px;color:#333;font-family:"Roboto",sans-serif;font-size:16px;padding:12px 18px}
.zip-next{position:absolute;left:986px;top:38px;width:116px;height:44px;background:#1f1f1f;color:var(--white);border-radius:3px;font-family:"Roboto",sans-serif;font-size:16px;text-align:center;line-height:44px}

/* features */
.features{position:absolute;top:711px;left:0;width:1200px;height:1627px;background:var(--paper)}
.feature{position:absolute;left:190px;width:820px;height:318px;border-bottom:1px dashed var(--line)}
.feature:last-child{border-bottom:0}
.feature-media{position:absolute;top:38px;width:244px;height:244px;border-radius:50%;border:2px dotted #9a9a9a;padding:10px}
.feature-media div{width:100%;height:100%;border-radius:50%}
.feature-body{position:absolute;top:58px;width:490px}
.feature h2{font-family:"Roboto",sans-serif;font-weight:400;font-size:32px;color:var(--ink);margin-bottom:16px}
.feature p{font-size:11.5px;line-height:21px;color:#444}
.read-more{margin-top:22px;padding:8px 20px;border-radius:17px;font-size:12.5px;background:#333}
.feature--right .feature-body{left:36px;text-align:right}
.feature--right .feature-media{left:548px}
.feature--left .feature-media{left:40px}
.feature--left .feature-body{left:313px;text-align:left}

/* testimonial */
.testimonial{position:absolute;top:2338px;left:0;width:1200px;height:223px;background:var(--white);border-top:1px solid #e6e6e6;text-align:center}
.quote-mark{position:absolute;font-family:Georgia,serif;font-size:34px;color:#444}
.testimonial p{position:absolute;left:210px;width:780px;top:38px;font-size:12px;line-height:21px;color:#666}
.testimonial cite{position:absolute;left:0;width:1200px;top:126px;font-style:normal;font-family:"Roboto",sans-serif;font-size:15px;color:#333}
.dots{position:absolute;left:0;width:1200px;top:168px;display:flex;justify-content:center;gap:8px}
.dots span{width:9px;height:9px;border-radius:50%;border:1.5px solid var(--blue)}
.dots span:first-child{background:var(--blue)}

/* footer */
.site-footer{position:absolute;top:2561px;left:0;width:1200px;height:208px;background:var(--footer);border-top:1px solid #e2e2e2}
.footer-col{position:absolute;top:28px;font-size:12.5px;line-height:22px;color:#333}
.footer-col h3{font-family:"Roboto",sans-serif;font-weight:400;font-size:17px;color:#333;margin-bottom:12px}
.footer-col--contact h3{font-weight:500}
.news-form{display:flex;gap:10px;margin-top:18px}
.news-input{width:188px;height:32px;border:1px solid #ddd;background:var(--white);font-size:10px;color:#888;padding:8px 12px}
.news-submit{height:32px;padding:0 12px;background:var(--blue);color:var(--white);font-size:12px;line-height:32px;border-radius:2px}
.follow{display:flex;gap:4px;margin-bottom:4px}
.follow span{font-size:9px;line-height:15px;border:1px solid #bbb;border-radius:3px;background:#fafafa;padding:0 6px}
.social{display:flex;gap:7px;margin-top:20px}
.social span{width:26px;height:26px;border-radius:50%;background:var(--social)}
.contact-address{font-size:12px;line-height:21px;display:block}
.contact-line{display:flex;align-items:center;gap:14px;margin-top:6px}

.copyright{position:absolute;top:2769px;left:0;width:1200px;height:66px;background:var(--bar);color:#ddd;font-size:13px;text-align:center;line-height:66px}
</style>
</head>
<body>

<header class="site-header">
  <div class="brand"><span class="brand-dot"></span>Turf Bloom</div>
  <nav class="main-nav">
    <a href="#">HOME</a><a href="#">ABOUT</a><a href="#">LAWN CARE SERVICES</a><a href="#">MAINTENANCE</a><a href="#">CONTACT US</a>
  </nav>
</header>

<section class="hero">
  <div class="hero-bg" role="img" aria-label="Hazy city skyline under a pale blue sky"></div>
  <h1 class="hero-title">SAME DAY &amp; NEXT DAY<br>LAWN CARE SERVICES</h1>
  <p class="hero-copy">Lorem ipsum dolor sit amet, consectetur adipiscing elit, sed do eiusmod tempor incididunt ut labore et dolore magna aliqua. Ut enim ad minim veniam, quis nostrud exercitation ullamco laboris nisi ut aliquip ex ea commodo consequat. Duis aute irure dolor in reprehenderit in voluptate velit esse cillum dolore eu fugiat nulla pariatur. Excepteur sint occaecat cupidatat non proident, sunt in culpa qui officia deserunt mollit anim id est laborum</p>
  <a class="btn-dark hero-cta" href="#">BOOK IN 60 SECS</a>
  <div class="video" role="img" aria-label="Video still of a lawn mower cutting green grass">
    <div class="video-play"><svg width="16" height="16" viewBox="0 0 16 16"><path d="M3 1l12 7-12 7z" fill="#fff"/></svg></div>
    <div class="video-bar"><div class="video-progress"><span></span></div></div>
  </div>
</section>

<section class="booking">
  <h2 class="booking-title">BOOK A LAWN CARE SERVICES IN 60 SECONDS</h2>
  <p class="booking-copy">Lorem ipsum dolor sit amet, consectetur adipiscing elit, sed do eiusmod tempor incididunt ut labore et dolore magna aliqua. Ut enim ad minim veniam,</p>
  <div class="zip-field">ZIP CODE</div>
  <div class="zip-next">NEXT</div>
</section>

<section class="features">
  <article class="feature feature--right" style="top:0">
    <div class="feature-body">
      <h2>No Contract</h2>
      <p>Lorem ipsum dolor sit amet, consectetur adipiscing elit, sed do eiusmod tempor incididunt ut labore et dolore magna aliqua. Ut enim ad minim veniam, quis nostrud exercitation ullamco laboris nisi ut aliquip ex ea commodo consequat. Duis aute irure dolor in reprehenderit in voluptate velit esse cillum dolore eu fugiat nulla pariatur.</p>
      <a class="btn-dark read-more" href="#">Read More</a>
    </div>
    <div class="feature-media"><div role="img" aria-label="Photo of a contract paper with a pen" style="background:var(--photo-paper)"></div></div>
  </article>
  <article class="feature feature--left" style="top:319px">
    <div class="feature-media"><div role="img" aria-label="Photo of a phone standing in green grass" style="background:var(--photo-sky)"></div></div>
    <div class="feature-body">
      <h2>Instant Scheduling</h2>
      <p>Lorem ipsum dolor sit amet, consectetur adipiscing elit, sed do eiusmod tempor incididunt ut labore et dolore magna aliqua. Ut enim ad minim veniam, quis nostrud exercitation ullamco laboris nisi ut aliquip ex ea commodo consequat. Duis aute irure dolor in reprehenderit in voluptate velit esse cillum dolore eu fugiat nulla pariatur.</p>
      <a class="btn-dark read-more" href="#">Read More</a>
    </div>
  </article>
  <article class="feature feature--right" style="top:631px">
    <div class="feature-body">
      <h2>Same Day Service</h2>
      <p>Lorem ipsum dolor sit amet, consectetur adipiscing elit, sed do eiusmod tempor incididunt ut labore et dolore magna aliqua. Ut enim ad minim veniam, quis nostrud exercitation ullamco laboris nisi ut aliquip ex ea commodo consequat. Duis aute irure dolor in reprehenderit in voluptate velit esse cillum dolore eu fugiat nulla pariatur.</p>
      <a class="btn-dark read-more" href="#">Read More</a>
    </div>
    <div class="feature-media"><div role="img" aria-label="Photo of a lawn mower on a green lawn" style="background:var(--photo-grass)"></div></div>
  </article>
  <article class="feature feature--left" style="top:952px">
    <div class="feature-media"><div role="img" aria-label="Photo of a dollar sign shaped hedge under a blue sky" style="background:var(--photo-hedge)"></div></div>
    <div class="feature-body">
      <h2>Fully Licensed and Insured</h2>
      <p>Lorem ipsum dolor sit amet, consectetur adipiscing elit, sed do eiusmod tempor incididunt ut labore et dolore magna aliqua. Ut enim ad minim veniam, quis nostrud exercitation ullamco laboris nisi ut aliquip ex ea commodo consequat. Duis aute irure dolor in reprehenderit in voluptate velit esse cillum dolore eu fugiat nulla pariatur.</p>
      <a class="btn-dark read-more" href="#">Read More</a>
    </div>
  </article>
  <article class="feature feature--right" style="top:1264px">
    <div class="feature-body">
      <h2>Money Back Guarantee</h2>
      <p>Lorem ipsum dolor sit amet, consectetur adipiscing elit, sed do eiusmod tempor incididunt ut labore et dolore magna aliqua. Ut enim ad minim veniam, quis nostrud exercitation ullamco laboris nisi ut aliquip ex ea commodo consequat. Duis aute irure dolor in reprehenderit in voluptate velit esse cillum dolore eu fugiat nulla pariatur.</p>
      <a class="btn-dark read-more" href="#">Read More</a>
    </div>
    <div class="feature-media"><div role="img" aria-label="Money back guarantee seal" style="background:var(--photo-seal)"></div></div>
  </article>
</section>

<section class="testimonial">
  <span class="quote-mark" style="left:170px;top:22px">&ldquo;</span>
  <p>Lorem ipsum dolor sit amet, ea doming epicuri iudicabit nam, te usu virtute placerat. Purto brute disputando cu est, eam dicam soluta ei. Vel dicam vivendo accusata ei, cum ne periculis molestiae pri. Lorem ipsum dolor sit amet, ea doming epicuri iudicabit nam. Lorem ipsum dolor sit amet, ea doming epicuri &nbsp; Lorem ipsum dolor sit amet, ea doming epicuri iudicabit nam, te usu virtute placerat.</p>
  <span class="quote-mark" style="left:1010px;top:82px">&rdquo;</span>
  <cite>JOHN DOE</cite>
  <div class="dots"><span></span><span></span><span></span></div>
</section>

<footer class="site-footer">
  <div class="footer-col" style="left:100px">
    <h3>Our Services</h3>
    No Contract<br>Instant Scheduling<br>Same Day Service<br>Fully Licensed and Insured,<br>Money Back Guarantee.
  </div>
  <div class="footer-col" style="left:313px;width:280px">
    <h3>Newsletter Subscription</h3>
    <span style="font-size:11.5px;line-height:19px;display:block">Lorem ipsum dolor sit amet, ea doming epicuri iudicabit nam, te usu virtute placerat. Purto brute disputando cu est, eam dicam soluta</span>
    <div class="news-form"><div class="news-input">Enter Your Email</div><div class="news-submit">Subscribe</div></div>
  </div>
  <div class="footer-col" style="left:668px">
    <h3>Connect With Us</h3>
    <div class="follow"><span>Follow</span><span>@turfbloom</span></div>
    <div class="follow"><span>Follow</span><span>105</span></div>
    <div class="social"><span></span><span></span><span></span><span></span><span></span></div>
  </div>
  <div class="footer-col footer-col--contact" style="left:897px;width:210px">
    <h3>Contact Us</h3>
    <span class="contact-address">4870 Meadowline Ave., Suite 12,<br>Fernbrook,</span>
    <div class="contact-line" style="margin-top:8px">
      <svg width="16" height="16" viewBox="0 0 16 16"><path d="M4 1l2.5 3-1.5 2c1 2 2.5 3.5 5 5l2-1.5 3 2.5-1.5 2.5C8 14 2 8 1.5 3z" fill="none" stroke="#555" stroke-width="1.2"/></svg>+1 555-014-8205
    </div>
    <div class="contact-line">
      <svg width="16" height="12" viewBox="0 0 16 12"><rect x=".6" y=".6" width="14.8" height="10.8" fill="none" stroke="#555" stroke-width="1.2"/><path d="M1 1l7 6 7-6" fill="none" stroke="#555" stroke-width="1.2"/></svg>info@turfbloom.com
    </div>
  </div>
</footer>

<div class="copyright">Copyright©2015 Turf Bloom</div>

</body>
</html>
```